Stationary, Envelope, Folder, Brochure
brightvesselhome.example
Stationary, Envelope, Folder, Brochure - Health
Creative Brief
Health
Corporate, and Patients. Something bright and uplifting to grab the brightvessel home feeling when people look at our materials. I like the QKR Floral Copper Heron logo and some of the materials they use. It has an uplifting look and feel.
Provide the materials listed in the Title. Use the uploaded picture logo.
quietharborkeeper quietharborkeeper
Colors: I do like the Blues and the gradient from a darker to a brighter blue. Maybe even do that more with other bright colors. Have fun explore a little and think outside the box. Will try to provide with as much feedback as possible. -Dorian
Hi Everyone, Keep in mind we want a look and feel of "BRIGHT Vessel Home" and putting the "Care" back into healthcare. Having a bright and professional look that will excite the senses when a person looks at the material. We do not want to be the "norm" of home health. Our clients are of all ages for example 20+. Lets get excited, creative, and see what we can come up with. Also "Brightvessel Home" Font needs to also be fun and represent the logo and spirit of the great experience our company provide unlike others.

```html
<!DOCTYPE html>
<html lang="en">
<head>
<meta charset="utf-8">
<title>Brightvessel Home – Stationery Set</title>
<link rel="stylesheet" href="https://fonts.googleapis.com/css2?family=Open+Sans:ital,wght@0,400;0,600;0,700;1,400&family=Questrial&display=swap">
<style>
:root{
  --bg:#ececec;
  --paper:#f7f7f7;
  --green:#1f8a3c;
  --green-dark:#0b6b3a;
  --green-bright:#3aa24c;
  --navy:#2b2f7a;
  --ink:#6f6f6f;
  --white:#ffffff;
}
*{box-sizing:border-box;margin:0;padding:0}
html,body{width:1200px;height:795px;overflow:hidden}
body{background:var(--bg);font-family:"Open Sans",sans-serif;color:var(--ink);position:relative}
.piece{position:absolute;background:var(--paper);box-shadow:0 2px 6px rgba(0,0,0,.12);overflow:hidden}
.wave{position:absolute;left:0;bottom:0;width:100%;display:block}
.brand-name{font-family:"Open Sans",sans-serif;font-weight:700;color:var(--green);text-transform:uppercase;letter-spacing:.02em;white-space:nowrap}

/* Business card front */
.card-front{left:40px;top:40px;width:250px;height:143px;background:radial-gradient(circle at 60% 45%,var(--green-bright),var(--green-dark));color:var(--white);text-align:center}
.card-front .brand-name{color:var(--white);font-size:17px;margin-top:50px}
.card-front .site{font-size:7px;letter-spacing:.15em;margin-top:20px;font-family:"Questrial",sans-serif}

/* Business card back */
.card-back{left:40px;top:205px;width:250px;height:143px}
.card-back .brand-name{position:absolute;left:16px;top:14px;font-size:11px}
.card-back .contacts{position:absolute;left:16px;top:44px;list-style:none;font-size:6.5px;line-height:11px}
.card-back .contacts li{display:flex;align-items:center;gap:5px}
.card-back .contacts svg{width:7px;height:7px}
.card-back .holder{position:absolute;right:16px;top:62px;text-align:right;font-size:6.5px;line-height:9px}
.card-back .holder strong{display:block;color:var(--navy);font-size:8px}

/* Letterhead */
.letterhead{left:330px;top:36px;width:320px;height:452px}
.letterhead .brand-name{position:absolute;right:28px;top:30px;font-size:15px}
.letterhead .meta{position:absolute;left:30px;top:86px;font-size:7px}
.letterhead .subject{color:var(--green);font-weight:600;letter-spacing:.12em;font-size:8px;margin-top:4px}
.letterhead .body{position:absolute;left:30px;right:30px;top:126px;font-size:6.5px;line-height:10px;font-style:italic}
.letterhead .body p{margin-bottom:8px}
.letterhead .footer{position:absolute;left:16px;right:16px;bottom:10px;color:var(--white);font-size:6px;display:flex;justify-content:space-between}

/* Folder */
.folder{left:700px;top:36px;width:320px;height:452px}
.folder .brand-name{position:absolute;right:26px;top:64px;font-size:19px}
.folder .site{position:absolute;left:0;right:0;bottom:70px;text-align:center;color:var(--white);font-family:"Questrial",sans-serif;font-size:11px;letter-spacing:.25em}

/* Envelope front */
.envelope-front{left:330px;top:530px;width:400px;height:200px}
.envelope-front .brand-name{position:absolute;left:26px;top:24px;font-size:13px}
.envelope-front .address{position:absolute;left:26px;top:46px;font-size:6px;font-style:italic}
.envelope-front .window{position:absolute;left:26px;top:66px;width:150px;height:46px;border-radius:6px;background:#e6e6e6;border:1px solid #dcdcdc}

/* Envelope back */
.envelope-back{left:760px;top:530px;width:400px;height:200px}
.envelope-back .flap{position:absolute;left:0;right:0;top:0;height:92px;border-radius:0 0 14px 14px;background:radial-gradient(circle at 50% 60%,var(--green-bright),var(--green-dark));display:flex;align-items:center;justify-content:center}
.envelope-back .brand-name{color:var(--white);font-size:12px}

/* Name presentation */
.name-lockup{position:absolute;left:40px;top:590px;width:260px;text-align:center}
.name-lockup .brand-name{font-size:22px}
</style>
</head>
<body>

<section class="piece card-front" aria-label="Business card front">
  <div class="brand-name">Brightvessel Home</div>
  <div class="site">www.brightvesselhome.example</div>
</section>

<section class="piece card-back" aria-label="Business card back">
  <div class="brand-name">Brightvessel Home</div>
  <ul class="contacts">
    <li><svg viewBox="0 0 10 10"><circle cx="5" cy="5" r="5" fill="#2b2f7a"/></svg>555 014 2290</li>
    <li><svg viewBox="0 0 10 10"><circle cx="5" cy="5" r="5" fill="#2b2f7a"/></svg>555 014 2291</li>
    <li><svg viewBox="0 0 10 10"><circle cx="5" cy="5" r="5" fill="#2b2f7a"/></svg>info@brightvesselhome.example</li>
    <li><svg viewBox="0 0 10 10"><circle cx="5" cy="5" r="5" fill="#2b2f7a"/></svg>www.brightvesselhome.example</li>
  </ul>
  <div class="holder"><strong>Tobin Ashcroft</strong>Manager<br>Linden Yard, Marrow Lane<br>Castlefold</div>
  <svg class="wave" viewBox="0 0 250 50" height="50" preserveAspectRatio="none">
    <defs><linearGradient id="cardWave" x1="0" x2="1"><stop offset="0" stop-color="#3aa24c"/><stop offset="1" stop-color="#0b6b3a"/></linearGradient></defs>
    <path d="M0,8 C70,30 150,34 250,26" fill="none" stroke="#2b2f7a" stroke-width="2"/>
    <path d="M0,12 C70,34 150,38 250,30 L250,50 L0,50 Z" fill="url(#cardWave)"/>
  </svg>
</section>

<section class="piece letterhead" aria-label="Letterhead">
  <div class="brand-name">Brightvessel Home</div>
  <div class="meta">
    <div>16 - September - 2013</div>
    <div class="subject">SUBJECT:</div>
  </div>
  <div class="body">
    <p>We are pleased to confirm your next home visit and the care plan we agreed together. Our nurses will arrive at the planned time and bring every item you need.</p>
    <p>Please keep this letter with your records. If anything changes before the visit, call our team and we will gladly adjust the schedule to suit you and your family.</p>
    <p>Thank you for trusting us with your care.</p>
  </div>
  <svg class="wave" viewBox="0 0 320 90" height="90" preserveAspectRatio="none">
    <defs><linearGradient id="letterWave" x1="0" x2="1"><stop offset="0" stop-color="#3aa24c"/><stop offset="1" stop-color="#0b6b3a"/></linearGradient></defs>
    <path d="M0,4 C90,40 200,58 320,50" fill="none" stroke="#2b2f7a" stroke-width="3"/>
    <path d="M0,10 C90,46 200,64 320,56 L320,90 L0,90 Z" fill="url(#letterWave)"/>
  </svg>
  <div class="footer">
    <span>Linden Yard, Marrow Lane, Castlefold</span>
    <span>555 014 2290</span>
    <span>info@brightvesselhome.example</span>
  </div>
</section>

<section class="piece folder" aria-label="Presentation folder">
  <div class="brand-name">Brightvessel Home</div>
  <svg class="wave" viewBox="0 0 320 190" height="190" preserveAspectRatio="none">
    <defs><linearGradient id="folderWave" x1="0" x2="1" y1="0" y2="1"><stop offset="0" stop-color="#3aa24c"/><stop offset="1" stop-color="#0b6b3a"/></linearGradient></defs>
    <path d="M0,2 C120,8 240,30 320,78" fill="none" stroke="#2b2f7a" stroke-width="4"/>
    <path d="M0,8 C120,14 240,36 320,84 L320,190 L0,190 Z" fill="url(#folderWave)"/>
  </svg>
  <div class="site">www.brightvesselhome.example</div>
</section>

<section class="piece envelope-front" aria-label="Envelope front">
  <div class="brand-name">Brightvessel Home</div>
  <div class="address">Linden Yard, Marrow Lane, Castlefold</div>
  <div class="window"></div>
  <svg class="wave" viewBox="0 0 400 70" height="70" preserveAspectRatio="none">
    <defs><linearGradient id="envWave" x1="0" x2="1"><stop offset="0" stop-color="#3aa24c"/><stop offset="1" stop-color="#0b6b3a"/></linearGradient></defs>
    <path d="M0,4 C120,30 260,44 400,40" fill="none" stroke="#2b2f7a" stroke-width="3"/>
    <path d="M0,10 C120,36 260,50 400,46 L400,70 L0,70 Z" fill="url(#envWave)"/>
  </svg>
</section>

<section class="piece envelope-back" aria-label="Envelope back">
  <div class="flap"><span class="brand-name">Brightvessel Home</span></div>
</section>

<section class="name-lockup" aria-label="Brand name">
  <div class="brand-name">Brightvessel Home</div>
</section>

</body>
</html>
```